A compelling brochure for a children's charity to encourage donations

We are looking for a 4-page A-4 booklet (1 x A3 page folded in half). the Hour of Kindness Foundation is a non-profit organisation that aims to reduce the incidence and impact of children's critical injury in Australia. The brochure will give people who are new to the charity, an overview of who we are, what we do, why we do it and how they can help. You can reference our website www.hourofkindness-kids.org.au for colours and styles. The final design should encourage people to make a donation by being positive and powerful.
Use the text in the uploaded files.
Non-Profit

```html
<!DOCTYPE html>
<html lang="en">
<head>
<meta charset="utf-8">
<title>Hour of Kindness Foundation – Brochure</title>
<link href="https://fonts.googleapis.com/css2?family=Open+Sans:ital,wght@0,400;0,600;0,700;0,800;1,400&family=Cabin:wght@500&family=Marcellus&display=swap" rel="stylesheet">
<style>
:root{
  --backdrop:#bfbd98;
  --paper:#ffffff;
  --magenta:#bb1a98;
  --orange:#f29a1d;
  --grey-arrow:#8a8478;
  --fold:#b4b08e;
}
*{margin:0;padding:0;box-sizing:border-box}
html,body{width:1200px;height:1000px;overflow:hidden;background:var(--backdrop)}
body{position:relative;font-family:"Open Sans",Arial,sans-serif;color:var(--magenta)}
.spread{position:absolute;left:276px;width:614px;display:flex}
.spread--outer{top:30px;height:435px}
.spread--inner{top:523px;height:437px}
.page{position:relative;width:307px;height:100%;background:var(--paper);overflow:hidden}
.page--streaked{background:linear-gradient(155deg,#fff 0%,#fff 35%,#f1efe6 48%,#fff 55%,#eeece2 70%,#fff 82%,#f4f2ea 100%)}
.page--streaked-left{background:linear-gradient(200deg,#fff 0%,#f0eee4 30%,#fff 45%,#ecebe0 60%,#fff 78%,#f3f1e8 100%)}
.fold{position:absolute;left:583px;top:0;width:1px;height:1000px;background:var(--fold)}
.abs{position:absolute}
p,li{font-size:5.5px;line-height:1.35}
.h{color:var(--orange);font-weight:700;font-size:6.8px;margin-top:5px}
.hl{color:var(--orange)}
.strong{font-weight:700}
.it{font-style:italic}
/* cover */
.brand{left:36px;top:20px;width:240px;font-family:"Marcellus",serif;font-size:36px;line-height:1.05;color:var(--magenta)}
.brand-dot{display:inline-block;width:20px;height:20px;border-radius:50%;background:var(--orange);margin-left:6px;vertical-align:middle}
.site{left:38px;top:128px;font-family:"Cabin",sans-serif;font-size:18.5px;color:var(--orange)}
.intro{left:30px;top:176px;width:247px}
.intro p{text-align:justify;font-size:6.3px}
.intro .h{font-size:8.5px}
.contact{right:30px;top:335px;text-align:right}
.contact p{font-size:6px;font-weight:700;line-height:1.45}
.contact .lbl{font-size:6.8px}
.portrait{left:54px;top:332px;width:82px;height:82px;border-radius:50%;border:3px solid #fff;box-shadow:0 0 0 1.5px var(--magenta);background:radial-gradient(circle at 45% 40%,#6a4bb0,#3b2a86 60%,#2a1f66)}
.portrait-quote{left:58px;top:385px;width:74px;text-align:center;color:#fff;font-size:5px;font-weight:700;line-height:1.2}
/* research page */
.hero{left:77px;top:29px;width:153px;height:119px;border:1.5px solid var(--magenta);background:linear-gradient(160deg,#f3c9a8,#e07a4f 45%,#c9362e 75%,#f0e6e0)}
.research{left:31px;top:164px;width:249px}
.research p{text-align:justify;font-size:5.2px;line-height:1.3}
.research .h{font-size:6.6px;margin-top:6px}
/* stats */
.stat{top:38px;width:81px;height:52px;border:1.5px solid var(--magenta);background:#fff;color:#111}
.stat--a{left:29px}.stat--b{left:114px}.stat--c{left:199px}
.stat-a1{font-weight:800;font-size:9px;position:absolute;left:4px;top:3px}
.stat-a2{font-weight:800;font-size:17px;position:absolute;left:4px;top:10px;color:var(--magenta)}
.stat-a3{font-size:5px;font-weight:700;position:absolute;left:4px;top:32px;line-height:1.25}
.stat-b1{position:absolute;left:0;top:3px;width:100%;text-align:center;font-weight:800;font-size:9px;color:var(--magenta)}
.stat-b1 span{color:var(--orange)}
.stat-b2{position:absolute;left:0;top:14px;width:100%;text-align:center;font-size:5.5px;font-weight:700;color:var(--orange)}
.stat-b3{position:absolute;left:0;top:20px;width:100%;text-align:center;font-size:9.5px;font-weight:800;color:var(--magenta)}
.stat-c1{position:absolute;left:4px;top:3px;width:74px;font-family:"Marcellus",serif;font-size:6.2px;line-height:1.2}
.stat-c2{position:absolute;left:28px;top:30px;width:40px;height:17px;border:1.5px solid #111;border-radius:3px;font-weight:800;font-size:12px;color:var(--magenta);text-align:center;line-height:15px}
.about{left:30px;top:104px;width:249px}
.about p{text-align:justify}
.didyou{font-size:8px;margin:8px 0 6px}
.facts li{list-style:none;margin-bottom:6px;padding-left:14px;text-indent:-14px}
.facts li::before{content:"•";display:inline-block;width:14px;text-indent:0}
.kids{left:42px;top:300px;width:237px;height:132px;border-radius:40px 40px 0 0;background:linear-gradient(180deg,rgba(255,255,255,0) 0%,#f2c7a6 25%,#e58a5c 55%,#d04d45 80%,#e9e2da 100%)}
/* evidence page */
.evidence{left:31px;top:44px;width:249px}
.evidence p{text-align:justify;margin-bottom:5px;font-size:5.2px;line-height:1.3}
.flow{left:31px;top:272px;width:249px;text-align:center}
.flow p{font-size:6px}
.arrow{display:block;margin:7px auto}
</style>
</head>
<body>
<div class="fold"></div>

<section class="spread spread--outer">
  <article class="page page--cover">
    <div class="abs brand">Hour of<br>Kindness<span class="brand-dot"></span></div>
    <div class="abs site">www.hourofkindness-kids.org.au</div>

    <div class="abs intro">
      <p class="h">The phone rings</p>
      <p>You are told there’s been an accident and your child, critically injured has been rushed to the Children’s Hospital at Riverbend.</p>
      <p class="hl it">What are you going to do?</p>
      <p style="margin-top:20px">A critical accident can happen to anyone’s child. It is unexpected and in an instant your life is irreversibly and dramatically changed. Your beloved child is suddenly in an unfamiliar hospital, connected to a dizzying array of mysterious equipment, surrounded by confident doctors and assertive nurses. <span class="hl it">Who are you? What is your role? Will your child survive? What about your job, your other children? How will you cope? Why did this happen to you?</span> These questions and the vital support of these children and their families are our inspiration, motivation and absolute reason for being. The work of the <span class="hl">Hour of Kindness Foundation</span> is solely to care for these extraordinarily vulnerable families.</p>
    </div>

    <div class="abs portrait" role="img" aria-label="Photo of a smiling child in a purple-lit hospital setting"></div>
    <p class="abs portrait-quote">“Please help other critically injured kids like me.”</p>

    <div class="abs contact">
      <p class="lbl">For All Enquiries:</p>
      <p style="margin-top:8px">Hour of Kindness Foundation Limited</p>
      <p class="hl">Suite 4, 12 Wattle Lane</p>
      <p class="hl">Northbridge NSW 2063</p>
      <p class="lbl" style="margin-top:10px">Contact: <span class="hl">Mara Collins</span></p>
      <p class="lbl">Ph. <span class="hl">02 5550 0199</span></p>
      <p class="lbl" style="margin-top:3px">Email: <span class="hl">enquiry@hourofkindness-kids.org.au</span></p>
    </div>
  </article>

  <article class="page page--streaked">
    <div class="abs hero" role="img" aria-label="Photo of a group of cheerful young children waving at the camera"></div>
    <div class="abs research">
      <p class="h" style="margin-top:0">The Paediatric Critical Injury Research Program</p>
      <p style="margin-top:7px">Developed and led by Associate Professor Jane Morrow of Harbour City University, Harbour City Nursing School, the 6-year $960,000 program will:</p>
      <p style="margin-top:5px">•&nbsp;&nbsp;&nbsp;&nbsp;Quantify exactly how and why many children are hospitalised in Australia as a result of severe injury.</p>
      <p>•&nbsp;&nbsp;&nbsp;&nbsp;Investigate whether ambulance protocols should be mandated to ensure that children are transported directly to a paediatric trauma centre.</p>
      <p>•&nbsp;&nbsp;&nbsp;&nbsp;Provide definitive answers regarding unmet needs in an Australia-wide, Australian first survey of parents of severely injured children.</p>
      <p>The program is currently on schedule and on budget.</p>
      <p class="h">Informed interventions</p>
      <p>Evidence gathered during the research program will inform interventions to be piloted by the Hour of Kindness Foundation. Prioritised interventions will focus on family support. Piloted interventions may include:</p>
      <p>•&nbsp;&nbsp;&nbsp;&nbsp;Appointment of in-hospital Family Support Coordinator service to assess and support at-risk families</p>
      <p>•&nbsp;&nbsp;&nbsp;&nbsp;Development of a resilience tool-kit for parents</p>
      <p>•&nbsp;&nbsp;&nbsp;&nbsp;A 24-hour help-line for parents and families of critically injured children</p>
      <p class="h">Measuring effectiveness</p>
      <p>The effectiveness of interventions will be measured against the data gathered during the Paediatric Critical Injury Research Program.</p>
      <p class="h">Advocacy</p>
      <p>Advocating improved care for thousands of Australian families, the most effective interventions and services identified will be included in recommendations for health policy change to Federal and State Health Departments. The Hour of Kindness Foundation’s ultimate objective is reducing the incidence and impact of children’s critical injury in Australia.</p>
    </div>
  </article>
</section>

<section class="spread spread--inner">
  <article class="page page--streaked-left">
    <div class="abs stat stat--a">
      <span class="stat-a1">MORE THAN</span>
      <span class="stat-a2">1000</span>
      <span class="stat-a3">children are hospitalised<br>with an injury each week</span>
    </div>
    <div class="abs stat stat--b">
      <span class="stat-b1">UP TO <span>40%</span></span>
      <span class="stat-b2">OF PARENTS SUFFER</span>
      <span class="stat-b3">DEPRESSION</span>
      <svg class="abs" style="left:6px;top:35px" width="68" height="12" viewBox="0 0 68 12" aria-hidden="true">
        <g fill="#222"><rect x="0" y="2" width="4" height="10" rx="2"/><rect x="7" y="2" width="4" height="10" rx="2"/><rect x="14" y="2" width="4" height="10" rx="2"/><rect x="21" y="2" width="4" height="10" rx="2"/></g>
        <g fill="#bbb"><rect x="28" y="2" width="4" height="10" rx="2"/><rect x="35" y="2" width="4" height="10" rx="2"/><rect x="42" y="2" width="4" height="10" rx="2"/><rect x="49" y="2" width="4" height="10" rx="2"/><rect x="56" y="2" width="4" height="10" rx="2"/><rect x="63" y="2" width="4" height="10" rx="2"/></g>
      </svg>
    </div>
    <div class="abs stat stat--c">
      <span class="stat-c1">The average distance from home to a paediatric trauma hospital is</span>
      <span class="stat-c2">239<span style="font-size:5px">km</span></span>
    </div>

    <div class="abs about">
      <p><span class="hl strong">The Hour of Kindness Foundation</span> was founded in 2004 by Tom Haverly and his wife, Grace Linden following the tragic and highly publicised accidents of their daughter Ella. It is a non-profit registered national charity based in Sydney and governed by an independent Board of Directors. The Foundation’s revenue is generated by donations, philanthropic grants and sponsorships.</p>
      <p>The purpose of the Hour of Kindness Foundation is to permanently reduce the incidence and impact of children’s critical injury in Australia.</p>
      <p class="h didyou">Did you know.....</p>
      <ul class="facts">
        <li>Injury is the leading cause of death for children aged between 1 and 14 in Australia.</li>
        <li>Approximately 1000 children are hospitalised each week; more than twice the number of children hospitalised with cancer, diabetes and asthma combined.</li>
        <li>More than 40% of parents of critically injured children suffer depression</li>
        <li>Severely injured children are three to six times more likely to survive their injuries if they receive definitive care at a paediatric trauma centre.</li>
        <li>Child injury is of such public health importance that the Australian government recently identified children aged 0-14 as a priority issue, but has not yet implemented any nationally coordinated injury prevention strategies to address it.</li>
      </ul>
    </div>
    <div class="abs kids" role="img" aria-label="Photo of four smiling children lying on their fronts with chins in hands"></div>
  </article>

  <article class="page page--streaked">
    <div class="abs evidence">
      <p>In 2012, a commissioned study by <span class="hl">Dr Nora Ashby of the Eastern State University</span> revealed a lack of centralised national data relating to children’s critical injury despite alarming statistics.<br>Dr Ashby’s study discovered that parents of injured children experience myriad emotional, mental and physical stressors which result in anxiety, depression, addictions, job-loss and collapse of the family unit. 60% of these parents are likely to meet the criteria for Acute Stress Disorder and 70% of parents report fatigue 6 months after their child’s discharge. A parent’s ability to cope with the stress associated with the injury will affect the quality of life of all members of the family, as parents have total responsibility for practical considerations such as accommodation, jobs, other children, transport, bill payment as well as holistic implications, however little is known from an Australian perspective with a paucity of evidence-based recommendations or solutions.</p>
      <p>Over several years, the Foundation delivered specialised medical equipment, technologically innovative machines, therapies and individual services to hospitals and families across the country.</p>
      <p>However, to permanently reduce the incidence and impact of children’s critical injury, we must better understand the breadth and depths of the challenges faced by these children and their families throughout the trauma journey, and assess the health-care system’s efficacy in addressing these challenges.</p>
      <p>Presently in Australia, we do not have adequate knowledge about who is injured, where they come from, what causes the injuries, how the families cope and whether or not families survive intact in the longer term.</p>
      <p>The first step in achieving the purpose of the Hour of Kindness Foundation is to gather evidence for change through the <span class="hl">Paediatric Critical Injury Research Program</span>. This pioneering program is led by <span style="font-size:6px">Associate Professor Jane Morrow of the Harbour City Nursing School, Harbour City University.</span></p>
    </div>

    <div class="abs flow">
      <p><span class="hl">Informed interventions</span> such as in-hospital family care co-ordinators and other direct services will be piloted by the Foundation.</p>
      <svg class="arrow" width="16" height="22" viewBox="0 0 16 22" aria-hidden="true"><path d="M5 0h6v12h5L8 22 0 12h5z" fill="var(--grey-arrow)"/></svg>
      <p>Their effectiveness will be <span class="hl">measured</span>.</p>
      <svg class="arrow" width="16" height="22" viewBox="0 0 16 22" aria-hidden="true"><path d="M5 0h6v12h5L8 22 0 12h5z" fill="var(--grey-arrow)"/></svg>
      <p>Ultimately <span class="hl">we will advocate</span> for systemic change where appropriate in order to reduce the incidence and impact of these tragic accidents.</p>
    </div>
  </article>
</section>
</body>
</html>
```